Harborline Athletics Presents Harborline Bodywork with Marguerite

I'm promoting my massage therapy business which is located in a personal one on one training gym. A few of the modalities I offer are:
Basic Relaxation -light or deep.
Medical Massage- specific work for a specific problem.
Reflexology- feet feet and more feet.
Thai Yoga- I stretch you.
Scalp and Feet- Mega tension relief.
For more details, information and to make an appointment call Marguerite at :712 408 5519. E mail: tulipbaker@quillmail.net
I was playing with this: Bring me your tired, aching, stressed-out body and give me a chance to work some magic. (I hate promoting myself and that was extreme for me.)

Target Market(s)

Gym members and walk-ins from the Midtown Kingston, NY neighborhood.

Industry/Entity Type

Business

Colors

Designer to choose colors to be used in the design.

Requirements
Must have
• My name and phone # and my e mail address.
Should not have
• Anything sexual. This is serious healing work done by a licenced professional so there can be no confusion as to intent.

```html
<!DOCTYPE html>
<html lang="en">
<head>
<meta charset="utf-8">
<title>Massage Therapy at Harborline Athletics</title>
<link href="https://fonts.googleapis.com/css2?family=Poppins:wght@600;700&family=Questrial&display=swap" rel="stylesheet">
<style>
  :root {
    --teal: #4cc3cf;
    --teal-soft: #8fd8e0;
    --grey: #a3a3a6;
    --ink: #3a3a3c;
    --paper: #fbfbfb;
    --skin-light: #f3ddc9;
    --skin-mid: #e2b898;
  }
  * { margin: 0; padding: 0; box-sizing: border-box; }
  html, body { width: 1200px; height: 900px; overflow: hidden; background: var(--paper); }
  .flyer {
    position: relative; width: 1200px; height: 900px; overflow: hidden;
    background: linear-gradient(180deg, #ffffff 0%, #f6f6f6 100%);
    font-family: "Questrial", sans-serif; color: var(--ink);
  }
  .title { position: absolute; left: 60px; top: 270px; }
  .title__main {
    font-family: "Poppins", sans-serif; font-weight: 700;
    font-size: 60px; line-height: 0.98; color: var(--grey); letter-spacing: 1px;
  }
  .title__sub { font-size: 22px; color: var(--teal); letter-spacing: 1px; margin-top: 6px; white-space: nowrap; }

  .service { position: absolute; display: flex; align-items: center; gap: 18px; }
  .service__icon {
    width: 130px; height: 130px; border-radius: 50%;
    border: 4px solid var(--teal); display: flex; align-items: center; justify-content: center; flex: none;
  }
  .service__figure { width: 96px; height: 96px; border-radius: 50%; background: var(--teal); opacity: 0.85; }
  .service__name { font-family: "Poppins", sans-serif; font-weight: 600; font-size: 22px; color: var(--ink); white-space: nowrap; }
  .service__note { font-size: 23px; line-height: 1.1; color: var(--teal-soft); white-space: nowrap; }

  .service--relax   { left: 400px; top: 130px; }
  .service--medical { left: 770px; top: 50px; }
  .service--reflex  { left: 90px;  top: 440px; }
  .service--thai    { left: 150px; top: 650px; }
  .service--scalp   { left: 900px; top: 300px; flex-direction: column; align-items: flex-start; gap: 14px; }
  .service--scalp .service__icon { margin-left: 10px; }

  .hand {
    position: absolute; left: 250px; top: 600px; width: 720px; height: 340px;
    border-radius: 60% 40% 0 0 / 70% 60% 0 0;
    background: radial-gradient(ellipse at 60% 30%, var(--skin-light) 0%, var(--skin-mid) 55%, rgba(201,146,114,0) 80%);
    opacity: 0.7;
  }
  .bubble {
    position: absolute; left: 450px; top: 290px; width: 390px; height: 390px; border-radius: 50%;
    background: radial-gradient(circle at 40% 35%, rgba(255,255,255,0.95) 0%, rgba(240,244,245,0.85) 60%, rgba(225,232,234,0.6) 100%);
    box-shadow: inset 0 0 30px rgba(180,190,195,0.35);
    display: flex; flex-direction: column; align-items: center; justify-content: center; text-align: center;
    font-family: "Poppins", sans-serif; font-weight: 600; font-size: 28px; line-height: 1.12; letter-spacing: 0.5px;
  }
  .bubble__lead { color: var(--grey); }
  .bubble__call { color: var(--teal); }

  .contact { position: absolute; left: 580px; top: 770px; font-size: 20px; color: var(--ink); white-space: nowrap; }
  .contact__line { display: flex; align-items: center; gap: 24px; margin-top: 8px; font-size: 22px; }
  .contact__item { display: flex; align-items: center; gap: 8px; }
  .contact__name { color: var(--teal); }
  .contact__glyph { width: 26px; height: 26px; flex: none; }
</style>
</head>
<body>
<main class="flyer">
  <header class="title">
    <h1 class="title__main">MASSAGE<br>THERAPY</h1>
    <p class="title__sub">AT HARBORLINE ATHLETICS</p>
  </header>

  <div class="hand" role="img" aria-label="Photo of an open hand, palm up, holding the message bubble"></div>

  <section class="service service--relax">
    <div class="service__icon"><div class="service__figure" role="img" aria-label="Icon of a person seated in meditation"></div></div>
    <div><h2 class="service__name">Basic Relaxation</h2><p class="service__note">-light or deep</p></div>
  </section>

  <section class="service service--medical">
    <div class="service__icon"><div class="service__figure" role="img" aria-label="Icon of a therapist working on a client on a table"></div></div>
    <div><h2 class="service__name">Medical Massage</h2><p class="service__note">- specific work<br>for a specific<br>problem</p></div>
  </section>

  <section class="service service--reflex">
    <div class="service__icon"><div class="service__figure" role="img" aria-label="Icon of hands massaging a foot"></div></div>
    <div><h2 class="service__name">Reflexology</h2><p class="service__note">- feet feet<br>and more<br>feet</p></div>
  </section>

  <section class="service service--thai">
    <div class="service__icon"><div class="service__figure" role="img" aria-label="Icon of an assisted stretch"></div></div>
    <div><h2 class="service__name">Thai Yoga</h2><p class="service__note">- I stretch you</p></div>
  </section>

  <section class="service service--scalp">
    <div class="service__icon"><div class="service__figure" role="img" aria-label="Icon of hands massaging a scalp"></div></div>
    <div><h2 class="service__name">Scalp and Feet</h2><p class="service__note">- Mega tension relief.</p></div>
  </section>

  <div class="bubble">
    <p class="bubble__lead">BRING ME<br>YOUR TIRED,<br>ACHING,<br>STRESSED-OUT BODY</p>
    <p class="bubble__call">AND GIVE ME A<br>CHANCE TO WORK<br>SOME MAGIC.</p>
  </div>

  <footer class="contact">
    <p>For more details, information and to make an appointment :</p>
    <div class="contact__line">
      <span class="contact__item">
        <svg class="contact__glyph" viewBox="0 0 26 26" aria-hidden="true"><circle cx="13" cy="13" r="13" fill="var(--teal)"/><path d="M9 7c1 0 2 2.5 2 3s-1 1-1 1.5 2 4 4.5 4.5c.5 0 1-1 1.5-1s3 1 3 2-1.5 2.5-2.5 2.5C11 19.5 6.5 14 6.5 10 6.5 8.5 8 7 9 7z" fill="#fff"/></svg>
        712 408 5519 <span class="contact__name">Marguerite</span>
      </span>
      <span class="contact__item">
        <svg class="contact__glyph" viewBox="0 0 26 26" aria-hidden="true"><circle cx="13" cy="13" r="13" fill="var(--teal)"/><rect x="6.5" y="8.5" width="13" height="9" rx="1" fill="#fff"/><path d="M6.5 9l6.5 5 6.5-5" fill="none" stroke="var(--teal)" stroke-width="1.4"/></svg>
        tulipbaker@quillmail.net
      </span>
    </div>
  </footer>
</main>
</body>
</html>
```